Stationery Set for Brelvo Company

I need to create full stationery design for my company; Business Cards, Envelops, Letter Heads, Calendar.
In the letter head and Envelops... only contact information and website links.
Our company is a Service Management company with different domains of innovative services including Technology Service Management, Education Services, Outsourcing Management, Events Management.
I need a modern and innovative design specially for the business card. I some transparent designs and I like it, but don't limit your innovation to what I mentioned. Sky is limit for your innovation.

Target Market(s)

Middle East & Africa

Industry/Entity Type

Business Management

Colors
34a7d8
0355a3
85acd3
86cae7
cee9f5
cfdeed
e4daeb
f3f1f8
ecf7fb

Requirements
Must have
• Name, Title, Email, Mobile
Nice to have
• We have multiple locations in USA, KSA, EGY, so I need ideas about how to include all contact details maybe QR / Barcode or something else.
• Please see our locations and contact information: www.gofarnix.example
Should not have
• Too much text

```html
<!DOCTYPE html>
<html lang="en">
<head>
<meta charset="utf-8">
<title>Brelvo Company Stationery</title>
<link href="https://fonts.googleapis.com/css2?family=Saira:wght@500;600&family=Arimo:wght@400;700&display=swap" rel="stylesheet">
<style>
:root{
  --bg:#f1f1f1;
  --paper:#ffffff;
  --edge:#e0e0e0;
  --blue:#2f66f2;
  --grey:#5e5e5e;
  --ink:#333333;
  --soft:#9a9a9a;
}
*{box-sizing:border-box;margin:0;padding:0}
html,body{width:1200px;height:937px;overflow:hidden;background:var(--bg)}
body{position:relative;font-family:"Arimo",Arial,sans-serif;color:var(--ink)}
.sheet{position:absolute;background:var(--paper);border:1px solid var(--edge);overflow:hidden}
.brand{position:absolute;display:flex;align-items:center;gap:5px;font-family:"Saira",sans-serif;font-weight:600;color:var(--blue);white-space:nowrap}
.brand-square{background:var(--blue);flex:none}
.band{position:absolute;display:flex;gap:3px}
.band-grey{background:var(--grey)}
.band-blue{background:var(--blue);color:#fff;font-family:"Saira",sans-serif;font-weight:500;display:flex;align-items:center;justify-content:center;letter-spacing:.3px}
.contacts{position:absolute;display:grid;grid-template-columns:1fr 1fr;column-gap:10px;row-gap:3px;font-size:4px;color:var(--soft)}
.contacts span{display:flex;align-items:center;gap:3px}
.contacts i{display:inline-block;width:5px;height:5px;background:var(--grey);flex:none}

/* letterhead */
.letterhead{left:185px;top:68px;width:388px;height:544px}
.letter{position:absolute;left:36px;top:136px;width:298px;font-size:5px;line-height:7.2px}
.letter p{margin:0}
.letter .salutation{margin-top:7px}
.letter .body-one{margin-top:7px}
.letter .body-two{margin-top:16px}
.letter .body-three{margin-top:30px}
.letter .closing{margin-top:14px}
.letter .sender{margin-top:17px}
.letter strong{font-weight:700}
.signature{width:28px;height:24px;background:linear-gradient(135deg,#d9d9d9,#bcbcbc);margin-top:4px;border-radius:3px}

/* folder */
.folder{left:636px;top:40px;width:458px;height:576px}

/* business cards */
.card-front{left:46px;top:658px;width:175px;height:96px}
.card-back{left:46px;top:785px;width:175px;height:99px}
.card-person{position:absolute;left:105px;top:9px;font-size:6px;font-weight:700;line-height:9px}
.card-person small{display:block;font-size:4px;font-weight:400;color:var(--soft);line-height:5px}

/* envelopes */
.envelope-front{left:265px;top:674px;width:431px;height:206px}
.envelope-back{left:737px;top:672px;width:431px;height:208px}
.flap{position:absolute;left:0;top:0;width:431px;height:72px;background:var(--blue);border-radius:6px 6px 48px 6px;color:#fff;font-family:"Saira",sans-serif;font-weight:500;font-size:15px;display:flex;align-items:center;justify-content:center;letter-spacing:.4px}
</style>
</head>
<body>

<!-- Letterhead -->
<section class="sheet letterhead">
  <div class="brand" style="left:16px;top:26px;font-size:15px"><span class="brand-square" style="width:10px;height:10px"></span>Brelvo Company</div>
  <div class="letter">
    <p>July 2, 2012</p>
    <p class="salutation"><strong>Dear Client,</strong><br>12 Harbor Lane, Riyadh</p>
    <p class="body-one">Thank you for choosing our team for the coming year. This letter confirms the scope of services agreed at our last meeting, covering technology service management, education services, outsourcing management and event support across our regional offices. Our project leads will contact you this week to plan the first steps, confirm the people involved on both sides and share a short timeline for your review. We will also send a summary of the service levels, reporting dates and the contact points for each domain, so that every request reaches the right desk without delay.</p>
    <p class="body-two">Please keep this letter for your records and share it with the people on your side who will work with us during the project. A signed copy will follow by post.</p>
    <p class="body-three">We look forward to a long and productive partnership with your organisation. Should any question arise, our service desk is open every working day and will answer quickly by phone or email. Our offices in the USA, Saudi Arabia and Egypt work as one team, so you can reach whichever location is closest to you at any time. Further details on locations, opening hours and contacts are listed at the foot of this page and on our website, and we welcome your feedback as the work moves forward.</p>
    <p class="closing">Best Regards,</p>
    <div class="signature" role="img" aria-label="Handwritten signature"></div>
    <p class="sender"><strong>Dana Whitlow</strong><br>Director<br><br>12 Harbor Lane, Riyadh</p>
  </div>
  <div class="band" style="left:0;top:487px;width:388px;height:16px">
    <div class="band-grey" style="width:118px"></div>
    <div class="band-blue" style="flex:1;font-size:9px">www.gofarnix.example</div>
  </div>
  <div class="contacts" style="left:8px;top:514px;width:372px;grid-template-columns:1fr auto">
    <span><i></i>12 Harbor Lane, Riyadh</span><span><i></i>support@gofarnix.example</span>
    <span><i></i>+966 555 0142</span><span><i></i>www.gofarnix.example</span>
    <span><i></i>info@gofarnix.example</span><span><i></i>events@gofarnix.example</span>
  </div>
</section>

<!-- Presentation folder -->
<section class="sheet folder">
  <div class="brand" style="left:0;right:0;justify-content:center;top:248px;font-size:30px;gap:10px"><span class="brand-square" style="width:20px;height:20px"></span>Brelvo Company</div>
  <div class="band" style="left:0;top:523px;width:458px;height:26px">
    <div class="band-grey" style="width:140px"></div>
    <div class="band-blue" style="width:316px;font-size:13px">www.gofarnix.example</div>
  </div>
</section>

<!-- Business card front -->
<section class="sheet card-front">
  <div class="brand" style="left:8px;top:12px;font-size:8px;gap:3px"><span class="brand-square" style="width:6px;height:6px"></span>Brelvo Company</div>
  <div class="card-person">OMAR HADDAD<small>MANAGER</small></div>
  <div class="band" style="left:0;top:42px;width:175px;height:15px">
    <div class="band-grey" style="width:52px"></div>
    <div class="band-blue" style="flex:1;font-size:6px">www.gofarnix.example</div>
  </div>
  <div class="contacts" style="left:8px;top:69px;width:160px">
    <span><i></i>12 Harbor Lane, Riyadh</span><span><i></i>www.gofarnix.example</span>
    <span><i></i>+966 555 0142</span><span><i></i>support@gofarnix.example</span>
    <span><i></i>info@gofarnix.example</span><span><i></i>events@gofarnix.example</span>
  </div>
</section>

<!-- Business card back -->
<section class="sheet card-back">
  <div class="brand" style="left:0;right:0;justify-content:center;top:41px;font-size:11px;gap:4px"><span class="brand-square" style="width:7px;height:7px"></span>Brelvo Company</div>
</section>

<!-- Envelope front -->
<section class="sheet envelope-front">
  <div class="brand" style="left:15px;top:24px;font-size:15px"><span class="brand-square" style="width:10px;height:10px"></span>Brelvo Company</div>
  <div class="band" style="left:0;top:146px;width:431px;height:20px">
    <div class="band-grey" style="width:132px"></div>
    <div class="band-blue" style="width:296px;font-size:11px">www.gofarnix.example</div>
  </div>
</section>

<!-- Envelope back -->
<section class="sheet envelope-back">
  <div class="flap">www.gofarnix.example</div>
</section>

</body>
</html>
```